Service Plan Sales Flyer

The Watchpost Depot (www.kelvamart.com) is a commercial security integrator that installs security cameras, access control, intrusion, two-way radios and perimeter security. We require a one page flyer for our service plan for new and existing customers. The price of the service plan is $299/yr and includes the following;
1. Discounted service rate of $118/hr
2. Free remote support ($85/hr without a plan)
3. Free remote training
4. Priority support

Please review our brochure attached and create a one page sales flyer with the end goal of having the client sign up for our annual service plan . The plan will automatically renew every year. Email sales@kelvamart.com.

Target Market(s)

commercial industrial clients - no residential

Industry/Entity Type

review our website at www.kelvamart.com

Colors
0054AA
0677BA
7BADD7
CADEEF
E8F1F8
EE7325
F08F49
F5BC92
FAE3D3
FDF4ED

Requirements
Must have
• call to action
Should not have
• too many colors

```html
<!DOCTYPE html>
<html lang="en">
<head>
<meta charset="utf-8">
<title>The Watchpost Depot – Service Plan Flyer</title>
<link href="https://fonts.googleapis.com/css2?family=Poppins:wght@400;500;600;700&display=swap" rel="stylesheet">
<style>
  :root{
    --navy:#1c2f5a;
    --red:#e8392f;
    --white:#ffffff;
    --mist:#eef1f6;
  }
  *{margin:0;padding:0;box-sizing:border-box}
  html,body{width:1200px;height:2232px;overflow:hidden;background:var(--white)}
  body{font-family:"Poppins",sans-serif;color:var(--navy);position:relative}
  .flyer{position:absolute;inset:0;overflow:hidden;background:var(--white)}

  .hero-shape{position:absolute;left:0;top:0;width:1200px;height:1400px}

  .brand{position:absolute;left:150px;top:120px;display:flex;align-items:center;gap:26px}
  .brand-mark{width:70px;height:70px;background:var(--navy)}
  .brand-name{font-weight:700;font-size:62px;color:var(--navy);letter-spacing:1px;text-transform:uppercase;line-height:1;white-space:nowrap}

  .camera-photo{position:absolute;right:60px;top:240px;width:230px;height:150px;border-radius:20px;
    background:linear-gradient(160deg,#f5f6f8,#c9ced6)}

  .strengths{position:absolute;left:50px;top:600px;list-style:none}
  .strengths li{display:flex;align-items:center;gap:20px;color:var(--white);font-weight:500;font-size:56px;margin-bottom:96px;line-height:1;white-space:nowrap}
  .strengths li svg{flex:none}

  .hero-illustration{position:absolute;left:610px;top:560px;width:540px;height:580px;border-radius:10px;
    background:linear-gradient(150deg,#fafbfc 0%,#dfe3ea 55%,#b9a089 100%);box-shadow:0 10px 30px rgba(0,0,0,.25)}

  .pricing{position:absolute;left:0;right:0;top:1420px;text-align:center;font-weight:500;font-size:56px;line-height:1.3;color:var(--navy)}
  .pricing .price{color:var(--red);font-weight:600}

  .benefits{position:absolute;left:90px;top:1600px;width:1020px;display:grid;grid-template-columns:1fr 1fr;gap:40px 34px}
  .benefit{height:150px;background:var(--navy);border-radius:26px;display:flex;align-items:center;gap:24px;padding:0 26px}
  .benefit-icon{flex:none;width:88px;height:88px;border-radius:50%;background:var(--red);display:flex;align-items:center;justify-content:center}
  .benefit-text{color:var(--white);font-size:28px;line-height:1.3;font-weight:400;white-space:nowrap}
  .benefit-text strong{font-weight:600}

  .renew-pill{position:absolute;left:50%;transform:translateX(-50%);top:1972px;height:64px;padding:0 52px;border-radius:32px;
    background:var(--red);color:var(--white);font-size:29px;font-weight:500;display:flex;align-items:center;white-space:nowrap}
  .renew-pill strong{font-weight:700;margin:0 8px}

  .cta{position:absolute;left:0;right:0;top:2066px;text-align:center;font-size:34px;font-weight:500;color:var(--red);white-space:nowrap}
  .cta strong{color:var(--navy);font-weight:700}

  .contact-bar{position:absolute;left:0;right:0;bottom:0;height:92px;background:var(--navy);display:flex;align-items:center;justify-content:space-between;padding:0 40px}
  .contact-item{display:flex;align-items:center;gap:14px;color:var(--white);font-size:25px;white-space:nowrap}
  .contact-item.phone{font-size:34px;font-weight:600}
  .contact-icon{width:46px;height:46px;border-radius:50%;background:var(--red);display:flex;align-items:center;justify-content:center;flex:none}
  .divider{width:2px;height:44px;background:rgba(255,255,255,.4);flex:none}
</style>
</head>
<body>
<main class="flyer">

  <svg class="hero-shape" viewBox="0 0 1200 1400" aria-hidden="true">
    <polygon points="0,320 600,320 1000,1320 0,1320" fill="var(--navy)"/>
    <polygon points="600,320 760,320 1160,1320 1000,1320" fill="var(--mist)"/>
    <polygon points="0,1150 0,1330 210,1330" fill="var(--red)"/>
    <polygon points="700,1140 980,1140 860,1310" fill="var(--red)"/>
  </svg>

  <header class="brand">
    <span class="brand-mark"></span>
    <span class="brand-name">The Watchpost Depot</span>
  </header>

  <div class="camera-photo" role="img" aria-label="Photo of a white dome security camera"></div>

  <ul class="strengths">
    <li><svg width="28" height="32" viewBox="0 0 30 34"><polygon points="0,0 30,17 0,34" fill="var(--red)"/></svg>Knowledgeable</li>
    <li><svg width="28" height="32" viewBox="0 0 30 34"><polygon points="0,0 30,17 0,34" fill="var(--red)"/></svg>Reliable</li>
    <li><svg width="28" height="32" viewBox="0 0 30 34"><polygon points="0,0 30,17 0,34" fill="var(--red)"/></svg>Easy</li>
  </ul>

  <div class="hero-illustration" role="img" aria-label="Illustration of an office door, a monitor showing camera footage and a bullet security camera"></div>

  <h1 class="pricing">The Service Plan Is Priced At <span class="price">$299/Year</span><br>and Includes The Following</h1>

  <section class="benefits">
    <div class="benefit">
      <span class="benefit-icon"><svg width="48" height="48" viewBox="0 0 50 50" fill="none" stroke="#fff" stroke-width="4"><circle cx="25" cy="25" r="21"/><line x1="16" y1="34" x2="34" y2="16"/><circle cx="17" cy="17" r="3.5"/><circle cx="33" cy="33" r="3.5"/></svg></span>
      <p class="benefit-text">Discounted Service<br>Rate Of $118/hr</p>
    </div>
    <div class="benefit">
      <span class="benefit-icon"><svg width="48" height="48" viewBox="0 0 50 50" fill="none" stroke="#fff" stroke-width="4"><path d="M8 30V24a17 17 0 0 1 34 0v6"/><rect x="6" y="28" width="9" height="13" rx="3"/><rect x="35" y="28" width="9" height="13" rx="3"/></svg></span>
      <p class="benefit-text">Free remote support,<br><strong>$85/hr</strong> without a plan</p>
    </div>
    <div class="benefit">
      <span class="benefit-icon"><svg width="48" height="48" viewBox="0 0 50 50" fill="none" stroke="#fff" stroke-width="4"><rect x="5" y="8" width="40" height="28" rx="3"/><line x1="18" y1="43" x2="32" y2="43"/><polygon points="21,15 32,22 21,29" fill="#fff" stroke="none"/></svg></span>
      <p class="benefit-text">Free remote training</p>
    </div>
    <div class="benefit">
      <span class="benefit-icon"><svg width="48" height="48" viewBox="0 0 50 50"><polygon points="25,4 31,18 46,19 34,29 38,44 25,36 12,44 16,29 4,19 19,18" fill="#fff"/></svg></span>
      <p class="benefit-text">Priority support</p>
    </div>
  </section>

  <p class="renew-pill">The plan will<strong>automatically</strong>renew every year</p>

  <p class="cta">Contact Us To Request a <strong>Free Quote</strong> and <strong>Security Plan</strong></p>

  <footer class="contact-bar">
    <span class="contact-item phone"><span class="contact-icon"><svg width="22" height="22" viewBox="0 0 24 24"><path d="M6 2l4 4-2 3a12 12 0 0 0 7 7l3-2 4 4-3 4C10 22 2 14 2 5z" fill="#fff"/></svg></span>1-877-555-0142</span>
    <span class="divider"></span>
    <span class="contact-item"><span class="contact-icon"><svg width="22" height="22" viewBox="0 0 24 24" fill="none" stroke="#fff" stroke-width="2"><rect x="2" y="5" width="20" height="14" rx="2"/><path d="M2 6l10 7 10-7"/></svg></span>sales@kelvamart.com</span>
    <span class="divider"></span>
    <span class="contact-item"><span class="contact-icon"><svg width="22" height="22" viewBox="0 0 24 24" fill="none" stroke="#fff" stroke-width="2"><circle cx="12" cy="12" r="10"/><ellipse cx="12" cy="12" rx="4" ry="10"/><line x1="2" y1="12" x2="22" y2="12"/></svg></span>www.kelvamart.com</span>
  </footer>

</main>
</body>
</html>
```